Harborstone Lending Business Card Design

We are looking for a nice looking business card design. I'd prefer something other than white for the background but white is ok if necessary. I'm uploading two versions of my picture, one is square and one is rounded. Also a couple of versions of the logo for white backgrounds as well as one for darker backgrounds.

Target Market(s)

Realtors and prospective clients

Industry/Entity Type

Mortgage

Contact Information for Business Card

Double sided business card. Not sure what is needed here.

Colors

Designer to choose colors to be used in the design.

Requirements
Must have
• Name: Marcus Pellham
• Title: Senior Mortgage Advisor
• Email: marcuspellham@harborstonelending.example
• website: www.marcuspellhamhomeloangroup.example
• Address: 4670 W 2850 N, STE 215 Salt Lake City, UT 84192
• Phone: 801-555-0187
• nmls# 948217
• Logo is on our webstie. www.harborstonelending.example
• Picture
Nice to have
• Colors could be similar to our website www.harborstonelending.example
• A list of what we do (VA Loans, FHA Loans, Conventional Loans, USDA Loans)

```html
<!DOCTYPE html>
<html lang="en">
<head>
<meta charset="utf-8">
<title>Harborstone Lending Business Card</title>
<link rel="stylesheet" href="https://fonts.googleapis.com/css2?family=Open+Sans:wght@400;600;700&display=swap">
<style>
  :root {
    --page-bg: #d3d3d3;
    --card-white: #ffffff;
    --brand-green: #7ca645;
    --name-green: #7aa63f;
    --ink: #1b1b1b;
    --photo-warm: #b9702c;
    --photo-deep: #4a4a3a;
  }
  * { margin: 0; padding: 0; box-sizing: border-box; }
  html, body { width: 1200px; height: 1200px; overflow: hidden; }
  body {
    background: var(--page-bg);
    font-family: "Open Sans", Arial, sans-serif;
    position: relative;
  }
  .card { position: absolute; width: 562px; background: var(--card-white); overflow: hidden; }
  .card-front { left: 327px; top: 194px; height: 325px; display: flex; align-items: center; justify-content: center; }
  .card-back { left: 333px; top: 618px; height: 317px; }

  .brand { display: flex; align-items: center; gap: 10px; color: var(--ink); }
  .brand-mark { width: 14px; height: 14px; background: var(--ink); border-radius: 50%; flex: none; }
  .brand-name { font-weight: 700; letter-spacing: 0.08em; text-transform: uppercase; white-space: nowrap; }
  .card-front .brand-name { font-size: 26px; }
  .card-back .brand-name { font-size: 17px; }
  .card-back .brand-mark { width: 11px; height: 11px; }

  .photo {
    position: absolute; left: 0; top: 0; width: 253px; height: 250px;
    background: linear-gradient(160deg, var(--photo-warm) 0%, #8a5a2a 40%, var(--photo-deep) 75%, #3c3f40 100%);
  }
  .identity {
    position: absolute; left: 0; top: 250px; width: 253px; height: 67px;
    text-align: center; padding-top: 13px;
  }
  .identity-name { color: var(--name-green); font-size: 16.5px; font-weight: 600; letter-spacing: 0.01em; line-height: 1; }
  .identity-title { color: var(--ink); font-size: 12.5px; font-weight: 400; margin-top: 3px; }

  .info-panel { position: absolute; left: 253px; top: 0; width: 309px; height: 317px; background: var(--brand-green); }
  .logo-box {
    position: absolute; left: 14px; top: 40px; width: 281px; height: 92px;
    background: var(--card-white); display: flex; align-items: center; justify-content: center;
  }
  .license {
    position: absolute; left: 14px; top: 144px; width: 281px;
    text-align: center; color: var(--card-white);
    font-size: 10.6px; font-weight: 600; letter-spacing: 0.06em;
  }
  .contact-list { position: absolute; left: 35px; top: 199px; list-style: none; }
  .contact-list li {
    display: flex; align-items: center; height: 21.5px;
    color: var(--card-white); font-size: 10.6px; white-space: nowrap;
  }
  .contact-list svg { width: 8px; height: 8px; margin-right: 11px; flex: none; fill: var(--card-white); }
  .contact-address { letter-spacing: -0.03em; }
</style>
</head>
<body>
  <section class="card card-front">
    <div class="brand">
      <span class="brand-mark"></span>
      <span class="brand-name">Harborstone Lending</span>
    </div>
  </section>

  <section class="card card-back">
    <div class="photo" role="img" aria-label="Portrait photo of Marcus Pellham outdoors with autumn foliage behind"></div>
    <div class="identity">
      <p class="identity-name">MARCUS PELLHAM</p>
      <p class="identity-title">Senior Mortgage Advisor</p>
    </div>
    <div class="info-panel">
      <div class="logo-box">
        <div class="brand">
          <span class="brand-mark"></span>
          <span class="brand-name">Harborstone Lending</span>
        </div>
      </div>
      <p class="license">NMLS# 948217</p>
      <ul class="contact-list">
        <li>
          <svg viewBox="0 0 10 10" aria-hidden="true"><path d="M2 0.5 L3.6 2.4 L2.7 3.6 Q3.6 5.8 6.3 7.3 L7.5 6.4 L9.5 8 L8.4 9.6 Q3.5 9 0.5 2 Z"/></svg>
          <span>801-555-0187</span>
        </li>
        <li>
          <svg viewBox="0 0 10 10" aria-hidden="true"><path d="M5 0 A3.5 3.5 0 0 1 8.5 3.5 C8.5 6 5 10 5 10 C5 10 1.5 6 1.5 3.5 A3.5 3.5 0 0 1 5 0 Z M5 2.2 A1.3 1.3 0 1 0 5 4.8 A1.3 1.3 0 1 0 5 2.2 Z" fill-rule="evenodd"/></svg>
          <span class="contact-address">4670 W 2850 N, STE 215 Salt Lake City, UT 84192</span>
        </li>
        <li>
          <svg viewBox="0 0 10 10" aria-hidden="true"><path d="M0 2 H10 V8 H0 Z M0.8 2.6 L5 5.6 L9.2 2.6" fill-rule="evenodd"/></svg>
          <span>marcuspellham@harborstonelending.example</span>
        </li>
        <li>
          <svg viewBox="0 0 10 10" aria-hidden="true"><circle cx="5" cy="5" r="4.6"/></svg>
          <span>www.marcuspellhamhomeloangroup.example</span>
        </li>
      </ul>
    </div>
  </section>
</body>
</html>
```